Copper Lantern Distillery Bourbon Barrel Aged Maple Syrup

we need a label made for a 375ml flask bottle for our bourbon barrel aged Maple Syrup .

Font styles to use
Sans Serif

Requirements
Must have
• Copper Lantern Distillery Logo, Maple Leaf, Bourbon Barrels,

```html
<!DOCTYPE html>
<html lang="en">
<head>
<meta charset="utf-8">
<title>Copper Lantern Distillery – Bourbon Barrel Aged Maple Syrup Label</title>
<link rel="stylesheet" href="https://fonts.googleapis.com/css2?family=Bungee+Shade&family=Old+Standard+TT:wght@700&family=Almendra:wght@400&display=swap">
<style>
  :root {
    --page: #ffffff;
    --parchment-light: #eee4d1;
    --parchment-dark: #d6c6a9;
    --edge: #9a8f80;
    --copper-rule: #7c4a28;
    --ink: #1a1612;
    --art-core: #b8a688;
    --art-fade: #d6c6a9;
  }
  html, body {
    margin: 0;
    padding: 0;
    width: 879px;
    height: 1200px;
    overflow: hidden;
    background: var(--page);
  }
  .label {
    display: block;
    width: 879px;
    height: 1200px;
  }
  .brand-name {
    font-family: "Old Standard TT", serif;
    font-weight: 700;
    fill: var(--ink);
  }
  .product-title {
    font-family: "Bungee Shade", sans-serif;
    fill: var(--ink);
  }
  .product-subtitle,
  .product-note,
  .product-volume {
    font-family: "Old Standard TT", serif;
    font-weight: 700;
    fill: var(--ink);
  }
  .product-name {
    font-family: "Almendra", serif;
    fill: var(--ink);
  }
  .leaf-icon {
    fill: var(--ink);
  }
</style>
</head>
<body>
<svg class="label" viewBox="0 0 879 1200" xmlns="http://www.w3.org/2000/svg">
  <defs>
    <radialGradient id="parchment" cx="50%" cy="45%" r="70%">
      <stop offset="0%" stop-color="var(--parchment-light)"/>
      <stop offset="100%" stop-color="var(--parchment-dark)"/>
    </radialGradient>
    <radialGradient id="barrel-tone" cx="50%" cy="50%" r="50%">
      <stop offset="0%" stop-color="var(--art-core)" stop-opacity="0.75"/>
      <stop offset="70%" stop-color="var(--art-core)" stop-opacity="0.35"/>
      <stop offset="100%" stop-color="var(--art-fade)" stop-opacity="0"/>
    </radialGradient>
    <linearGradient id="ribbon-tone" x1="0" y1="0" x2="1" y2="0">
      <stop offset="0%" stop-color="var(--art-core)" stop-opacity="0"/>
      <stop offset="15%" stop-color="var(--art-core)" stop-opacity="0.35"/>
      <stop offset="85%" stop-color="var(--art-core)" stop-opacity="0.35"/>
      <stop offset="100%" stop-color="var(--art-core)" stop-opacity="0"/>
    </linearGradient>
  </defs>

  <!-- Label body -->
  <path class="label-shape"
        d="M2,175 Q2,30 180,16 Q440,-4 699,16 Q877,30 877,175 V1025 Q877,1182 700,1196 H180 Q2,1182 2,1025 Z"
        fill="url(#parchment)" stroke="var(--edge)" stroke-width="2"/>
  <path class="label-rule"
        d="M24,185 Q24,52 190,38 Q440,20 689,38 Q855,52 855,185 V1015 Q855,1160 690,1174 H190 Q24,1160 24,1015 Z"
        fill="none" stroke="var(--copper-rule)" stroke-width="6"/>

  <!-- Distillery name in place of logo -->
  <g class="brand">
    <text class="brand-name" x="440" y="218" text-anchor="middle" font-size="56" textLength="480" lengthAdjust="spacingAndGlyphs">COPPER LANTERN</text>
    <text class="brand-name" x="440" y="280" text-anchor="middle" font-size="42" letter-spacing="7">DISTILLERY</text>
  </g>

  <!-- Title -->
  <text class="product-title" x="448" y="488" text-anchor="middle" font-size="86" textLength="730" lengthAdjust="spacingAndGlyphs">BOURBON BARREL</text>
  <text class="product-subtitle" x="443" y="558" text-anchor="middle" font-size="44">AGED</text>

  <!-- Barrel and ribbon artwork area -->
  <g class="artwork" role="img" aria-label="Engraved wooden bourbon barrel on a stand above a curling ribbon banner">
    <ellipse cx="440" cy="712" rx="190" ry="140" fill="url(#barrel-tone)"/>
    <path d="M80,760 Q260,800 440,840 Q620,800 845,760 L845,900 Q640,960 440,1010 Q240,960 80,900 Z"
          fill="url(#ribbon-tone)"/>
  </g>

  <!-- Product name on ribbon -->
  <g class="product-name-line" transform="rotate(-5 440 945)">
    <text class="product-name" x="268" y="966" text-anchor="middle" font-size="98" textLength="262" lengthAdjust="spacingAndGlyphs">Maple</text>
    <path class="leaf-icon" role="img" aria-label="Maple leaf"
          transform="translate(440 948) scale(1.15)"
          d="M0,-20 L4,-11 L9,-14 L7,-3 L15,-9 L13,-3 L20,-2 L14,4 L16,8 L6,7 L5,11 L1,8 L1,20 L-1,20 L-1,8 L-5,11 L-6,7 L-16,8 L-14,4 L-20,-2 L-13,-3 L-15,-9 L-7,-3 L-9,-14 L-4,-11 Z"/>
    <text class="product-name" x="622" y="966" text-anchor="middle" font-size="98" textLength="272" lengthAdjust="spacingAndGlyphs">Syrup</text>
  </g>

  <!-- Details -->
  <text class="product-note" x="446" y="1067" text-anchor="middle" font-size="31" textLength="276" lengthAdjust="spacingAndGlyphs">ALCOHOL FREE</text>
  <text class="product-volume" x="443" y="1132" text-anchor="middle" font-size="52" textLength="367" lengthAdjust="spacing">12.6 oz 375ml</text>
</svg>
</body>
</html>
```